Pantry Circle is an online food market place that connects foodies who make or grow great food with

We would like a 1/2 A4 page size flyer in landscape to promote our new business. We would like to encourage new home foodies to sign up for a membership on our website www.pantrycirclenz.co.nz and we would like customers who are looking for great food in their local community to search our website for their closest home foodie and support a neighbour who is growing or producing creative food locally

Target Market(s)

Creative food lovers

Industry/Entity Type

Landscape

Colors
acd037
f78f20
33b8a4

Requirements
Must have
• Food images and look groovy
• Must be easy to read and stand out on a notice board
• Website address www.pantrycirclenz.co.nz
Nice to have
• We wish to use this flyer in multiple locations and wish to put in different contact details prior to printing

```html
<!DOCTYPE html>
<html lang="en">
<head>
<meta charset="utf-8">
<title>Pantry Circle – Flyer</title>
<link rel="stylesheet" href="https://fonts.googleapis.com/css2?family=Montserrat:wght@700;800&family=Arimo:wght@700&display=swap">
<style>
  :root {
    --leaf-green: #3fae04;
    --lime: #acd037;
    --bark: #3a2314;
    --wood: #8a5a33;
    --kraft: #c9a77c;
    --orange: #f78f20;
    --white: #ffffff;
  }
  html, body {
    margin: 0;
    width: 1200px;
    height: 900px;
    overflow: hidden;
    background: var(--white);
  }
  .flyer {
    position: relative;
    width: 1200px;
    height: 900px;
  }
  .flyer__art {
    position: absolute;
    inset: 0;
  }
  .brand {
    position: absolute;
    left: 95px;
    top: 95px;
    width: 330px;
    height: 330px;
    display: flex;
    align-items: center;
    justify-content: center;
  }
  .brand__disc {
    position: absolute;
    inset: 0;
    border-radius: 50%;
    background: var(--kraft);
  }
  .brand__name {
    position: relative;
    margin: 0;
    font-family: "Montserrat", sans-serif;
    font-weight: 800;
    font-size: 46px;
    line-height: 1.05;
    text-align: center;
    color: var(--bark);
    text-transform: uppercase;
  }
  .headline {
    position: absolute;
    left: 440px;
    top: 96px;
    width: 700px;
    margin: 0;
    font-family: "Montserrat", sans-serif;
    font-weight: 800;
    font-size: 27px;
    line-height: 40px;
    text-align: center;
    color: var(--white);
    text-transform: uppercase;
    white-space: nowrap;
  }
  .headline__accent { color: var(--bark); }
  .pitch {
    position: absolute;
    right: 105px;
    top: 352px;
    width: 760px;
    font-family: "Arimo", sans-serif;
    font-weight: 700;
    font-size: 21.5px;
    line-height: 25px;
    color: var(--white);
    text-align: right;
    white-space: nowrap;
  }
  .pitch p { margin: 0 0 25px; }
  .pitch__rule {
    position: absolute;
    left: 1104px;
    top: 355px;
    width: 7px;
    height: 143px;
    background: var(--orange);
  }
  .info-band {
    position: absolute;
    left: 28px;
    top: 733px;
    width: 1144px;
    height: 48px;
    background: rgba(247, 143, 32, 0.85);
    display: flex;
    align-items: center;
    justify-content: center;
    gap: 10px;
    font-family: "Arimo", sans-serif;
    font-weight: 700;
    white-space: nowrap;
  }
  .info-band__lead { color: var(--lime); font-size: 32px; }
  .info-band__url { color: var(--white); font-size: 34px; }
</style>
</head>
<body>
<main class="flyer">
  <svg class="flyer__art" width="1200" height="900" viewBox="0 0 1200 900">
    <defs>
      <linearGradient id="wood-tones" x1="0" y1="0" x2="0" y2="1">
        <stop offset="0" stop-color="#8f5d34"/>
        <stop offset="1" stop-color="#6e4422"/>
      </linearGradient>
      <linearGradient id="produce-tones" x1="0" y1="0" x2="1" y2="0">
        <stop offset="0" stop-color="#e0a418"/>
        <stop offset="0.14" stop-color="#f0b81c"/>
        <stop offset="0.22" stop-color="#6fae2a"/>
        <stop offset="0.34" stop-color="#d8321e"/>
        <stop offset="0.52" stop-color="#b8221a"/>
        <stop offset="0.66" stop-color="#4f8a22"/>
        <stop offset="0.78" stop-color="#3f7a1c"/>
        <stop offset="0.86" stop-color="#e8672a"/>
        <stop offset="1" stop-color="#e05a22"/>
      </linearGradient>
    </defs>
    <rect role="img" aria-label="Photo of a wooden plank table top"
          x="28" y="230" width="1144" height="623" fill="url(#wood-tones)"/>
    <path role="img" aria-label="Photo of fresh yellow and green peppers, tomatoes, red and green chillies and carrots laid on the table"
          d="M28 540 Q140 440 300 430 Q420 560 560 580 Q720 480 860 480 Q1000 540 1172 560 V853 H28 Z"
          fill="url(#produce-tones)"/>
    <path class="green-field" d="M28 47 H1172 V255 Q640 215 28 560 Z" fill="var(--leaf-green)"/>
    <path class="curve-line" d="M1172 255 Q640 215 28 560" fill="none" stroke="var(--bark)" stroke-width="9"/>
  </svg>

  <div class="brand">
    <span class="brand__disc"></span>
    <p class="brand__name">Pantry<br>Circle</p>
  </div>

  <h1 class="headline">
    Be part of our exciting <span class="headline__accent">new online</span><br><span class="headline__accent">food marketplace</span> connecting<br>foodies in your local community
  </h1>

  <div class="pitch">
    <p>As a foodie you can sell your beautiful home produced<br>or home grown produce on our marketplace website</p>
    <p>As a food lover you can purchase lovingly grown or prepared<br>food and support your local foodie community while keeping<br>your food miles low</p>
  </div>
  <span class="pitch__rule"></span>

  <div class="info-band">
    <span class="info-band__lead">For more information go to:</span>
    <span class="info-band__url">WWW.PANTRYCIRCLENZ.CO.NZ</span>
  </div>
</main>
</body>
</html>
```